Business Card Design

We need a business card design that can also be aplied for postcards. We are a small indie record company that also do consulting, and development of independat artitst . I already have the name and the basic idea of what i am looking for but i am open to any suggestion.
Info for the card
Name of the company : Velmora Records
NAME : Tomas Invaldi
PHONE : 208-5536142
EMAIL : hello@velmorarecords.example
WEB: www.velmorarecords.example
Target Market(s)
Male - Female independent musicians ages 18 to 45
Industry/Entity Type
Record Company
Contact Information for Business Card
Independant records company that also works in consulting for music business models for independent artists
Look and feel
Each slider illustrates characteristics of the customer's brand and the style your logo design should communicate.

```html
<!DOCTYPE html>
<html lang="en">
<head>
<meta charset="utf-8">
<title>Velmora Records – Business Card</title>
<link href="https://fonts.googleapis.com/css2?family=Libre+Baskerville:wght@700&display=swap" rel="stylesheet">
<style>
  :root {
    --paper: #ffffff;
    --blue-deep: #0b4ea6;
    --blue-mid: #2a7cc7;
    --blue-light: #72b8e6;
    --band-line: #0d4d9e;
    --band-fill: rgba(120, 170, 225, 0.35);
    --ink: #141414;
    --text-light: #ffffff;
    --tape-dark: #111111;
    --tape-light: #f2f2f2;
  }
  html, body {
    margin: 0;
    padding: 0;
    width: 1200px;
    height: 702px;
    overflow: hidden;
    background: var(--paper);
  }
  .card {
    position: relative;
    width: 1200px;
    height: 702px;
    background: var(--paper);
  }
  .card-face {
    position: absolute;
    left: 22px;
    top: 22px;
    width: 1160px;
    height: 660px;
    background: radial-gradient(ellipse 55% 60% at 50% 48%, var(--blue-light) 0%, var(--blue-mid) 50%, var(--blue-deep) 100%);
    overflow: hidden;
  }
  .brand-band {
    position: absolute;
    left: 0;
    top: 143px;
    width: 1060px;
    height: 184px;
    background: var(--band-fill);
    border-top: 2px solid var(--band-line);
    border-bottom: 2px solid var(--band-line);
  }
  .brand-name {
    position: absolute;
    left: 62px;
    top: 198px;
    margin: 0;
    font-family: "Libre Baskerville", Georgia, serif;
    font-weight: 700;
    font-size: 60px;
    line-height: 1;
    color: var(--ink);
    letter-spacing: 0.5px;
  }
  .tape-art {
    position: absolute;
    left: 720px;
    top: 143px;
    width: 450px;
    height: 188px;
    background: linear-gradient(160deg, var(--tape-light) 0%, #9a9a9a 35%, var(--tape-dark) 60%, #3a3a3a 100%);
    clip-path: polygon(4% 2%, 93% 0%, 100% 60%, 30% 100%, 12% 100%);
  }
  .contact-name {
    position: absolute;
    left: 61px;
    top: 548px;
    margin: 0;
    font-family: "Libre Baskerville", Georgia, serif;
    font-weight: 700;
    font-size: 37px;
    color: var(--text-light);
  }
  .phone-icon {
    position: absolute;
    left: 689px;
    top: 466px;
    width: 98px;
    height: 130px;
  }
  .phone-number {
    position: absolute;
    left: 798px;
    top: 548px;
    margin: 0;
    font-family: "Libre Baskerville", Georgia, serif;
    font-weight: 700;
    font-size: 37px;
    color: var(--text-light);
  }
</style>
</head>
<body>
  <div class="card">
    <div class="card-face">
      <div class="brand-band"></div>
      <h1 class="brand-name">Velmora Records</h1>
      <div class="tape-art" role="img" aria-label="Illustration of a black and white audio cassette tape"></div>

      <p class="contact-name">Tomas Invaldi</p>

      <svg class="phone-icon" viewBox="0 0 98 130" aria-hidden="true">
        <path fill="var(--ink)" d="M22 4 C12 8 2 18 2 34 C2 62 22 100 48 122 C58 130 70 130 80 124 L94 116 C98 113 98 108 95 104 L78 84 C75 80 70 80 67 83 L58 90 C50 84 34 58 32 44 L42 38 C46 36 47 31 45 27 L36 6 C34 2 28 1 22 4 Z"/>
      </svg>
      <p class="phone-number">208-5536142</p>
    </div>
  </div>
</body>
</html>
```